Professionelles Design für Use Case Präsentationen im B2B-Bereich

Wir sind ein Schweizer Technologieunternehmen (Kalvor GmbH, www.kalvor.ch), das datenbasierte Simulationen, Optimierung und Entscheidungsunterstützung für Unternehmen in Logistik, Produktion und Verkehr anbietet.
Ziel dieses Projekts ist es, bestehende Use Cases in ein modernes, visuell ansprechendes Format zu bringen, das unsere Kompetenz und den Nutzen für Kunden klar kommuniziert. Die Zielgruppe sind Entscheidungsträger in mittleren bis großen Industrieunternehmen (Bereichsleiter, Projektleiter, Geschäftsleitung).
Was wir brauchen:
– Ein cleanes, professionelles Design (PowerPoint oder PDF-Layout), das sich gut für Präsentationen, Whitepaper oder als LinkedIn-Content eignet.
– Klare Struktur mit Infografiken, Icons, Diagrammen oder Visualisierungen.
– Integration unseres Logos, Farbschemas und ggf. unseres Slogans.
Stilrichtung:
– Modern, technisch fundiert, aber nicht überladen
– Klar, direkt, seriös
– Gerne mit einem visuellen roten Faden (z. B. durchgängige Icons oder Layout-Struktur)
Ein Beispieldokument (UseCase Transportkosten) mit Inhalte ist angefügt. Ziel ist eine wiederverwendbare Vorlage, die wir für verschiedene Kunden-Use-Cases adaptieren können.
- Roboto

```html
<!DOCTYPE html>
<html lang="en">
<head>
<meta charset="utf-8">
<title>Kalvor – Use Case Slides</title>
<link href="https://fonts.googleapis.com/css2?family=Montserrat:wght@400;500;600;700;800&display=swap" rel="stylesheet">
<style>
  :root{
    --stage:#8f8f8f;
    --paper:#f4f4f4;
    --lime:#dfdf7b;
    --olive:#9a9a55;
    --ink:#1c1c1c;
    --text:#444;
    --black:#050505;
    --white:#fff;
  }
  *{box-sizing:border-box;margin:0;padding:0}
  html,body{width:1078px;height:1200px;overflow:hidden}
  body{background:var(--stage);position:relative;font-family:'Montserrat',sans-serif;color:var(--ink)}
  .slide{position:absolute;left:89px;width:900px;height:506px;overflow:hidden;
    background:linear-gradient(125deg,#f7f7f7 0%,#efefef 35%,#f8f8f8 55%,#ececec 80%,#f6f6f6 100%);
    box-shadow:0 8px 14px rgba(0,0,0,.28)}
  .slide--overview{top:70px}
  .slide--results{top:619px}
  .accent{position:absolute;left:52px;top:0;width:158px;height:3px;background:var(--lime)}
  .slide-title{position:absolute;left:52px;top:20px;font-size:24px;font-weight:800;letter-spacing:.5px}
  .brand{position:absolute;right:52px;top:15px;display:flex;align-items:center;gap:8px}
  .brand-dot{width:36px;height:36px;border-radius:50%;background:var(--ink)}
  .brand-name{font-size:24px;font-weight:700;color:var(--ink)}
  .headline{position:absolute;left:97px;top:79px;width:707px;height:24px;background:var(--lime);
    font-size:16px;font-weight:700;text-align:center;line-height:24px;letter-spacing:.1px}
  .band{position:absolute;left:0;top:256px;width:100%;height:47px;background:var(--lime)}
  .diagram{position:absolute;left:0;top:0}
  .block{position:absolute;width:200px;font-size:8.9px;line-height:11.8px;color:var(--text)}
  .block h3{font-size:12.5px;line-height:14px;font-weight:700;color:var(--ink)}
  .block h3 span{font-weight:400;display:block}
  .block p{margin-top:6px}
  .block--left{left:55px;text-align:right}
  .block--right{left:646px;text-align:left}
  .footer{position:absolute;left:52px;top:455px;width:797px;height:34px;background:var(--black);
    color:var(--white);font-size:9px;font-weight:700;display:flex;align-items:center;padding:0 22px 0 16px}
  .footer .cta-label{color:var(--lime);margin-right:3px}
  .footer .contact{margin-left:auto;display:flex;align-items:center}
  .footer .item{display:flex;align-items:center;gap:10px}
  .footer .sep{width:1px;height:18px;background:#666;margin:0 16px 0 14px}
  .shot{position:absolute;background:var(--white);box-shadow:0 2px 6px rgba(0,0,0,.15)}
  .shot .fill{position:absolute;inset:7px}
  .shot--map{left:145px;top:179px;width:306px;height:187px}
  .shot--map .fill{background:linear-gradient(135deg,#c9d9b3,#dfe6cf 45%,#c8d7bd 70%,#b9cbd6)}
  .shot--dash{left:479px;top:133px;width:276px;height:275px}
  .shot--dash .fill{background:linear-gradient(180deg,#fafafa 0%,#e4e4e4 40%,#f5f5f5 65%,#ececec 100%);border:1px solid #ccc}
</style>
</head>
<body>

<section class="slide slide--overview">
  <div class="accent"></div>
  <h1 class="slide-title">WHAT IF</h1>
  <div class="brand"><span class="brand-dot"></span><span class="brand-name">Kalvor</span></div>
  <h2 class="headline">YOU COULD COMPARE NEW LOCATIONS WITH REAL TRANSPORTATION COSTS?</h2>
  <div class="band"></div>

  <svg class="diagram" width="900" height="506" viewBox="0 0 900 506">
    <defs>
      <radialGradient id="quad" cx="450" cy="278" r="150" gradientUnits="userSpaceOnUse">
        <stop offset="0.45" stop-color="#050505"/>
        <stop offset="1" stop-color="#5a5a5a"/>
      </radialGradient>
      <clipPath id="disc"><circle cx="450" cy="278" r="145"/></clipPath>
    </defs>
    <g clip-path="url(#disc)" fill="url(#quad)">
      <rect x="300" y="128" width="147.5" height="147.5"/>
      <rect x="452.5" y="128" width="147.5" height="147.5"/>
      <rect x="300" y="280.5" width="147.5" height="147.5"/>
      <rect x="452.5" y="280.5" width="147.5" height="147.5"/>
    </g>
    <circle cx="450" cy="278" r="58" fill="#8e8e4c" opacity=".85"/>
    <circle cx="450" cy="278" r="47" fill="var(--lime)"/>
    <circle cx="450" cy="278" r="43" fill="var(--white)"/>
    <circle cx="450" cy="278" r="26" fill="var(--ink)"/>

    <g stroke="var(--lime)" stroke-width="1.3">
      <line x1="274" y1="169" x2="317" y2="169"/><line x1="582" y1="169" x2="625" y2="169"/>
      <line x1="274" y1="388" x2="317" y2="388"/><line x1="582" y1="388" x2="625" y2="388"/>
    </g>
    <g fill="var(--ink)" stroke="var(--lime)" stroke-width="1.5">
      <circle cx="274" cy="169" r="2.5"/><circle cx="625" cy="169" r="2.5"/>
      <circle cx="274" cy="388" r="2.5"/><circle cx="625" cy="388" r="2.5"/>
    </g>

    <g fill="var(--lime)" stroke="var(--white)" stroke-width="3">
      <circle cx="357" cy="169" r="28"/><circle cx="542" cy="169" r="28"/>
      <circle cx="357" cy="388" r="28"/><circle cx="542" cy="388" r="28"/>
    </g>
    <!-- pin -->
    <path d="M357 159a7 7 0 0 0-7 7c0 5 7 12 7 12s7-7 7-12a7 7 0 0 0-7-7z" fill="var(--ink)"/>
    <circle cx="357" cy="166" r="2.6" fill="var(--lime)"/>
    <!-- briefcase -->
    <rect x="532" y="163" width="20" height="14" rx="2" fill="var(--ink)"/>
    <rect x="538" y="159" width="8" height="5" rx="1" fill="none" stroke="var(--ink)" stroke-width="2"/>
    <rect x="532" y="169" width="20" height="1.5" fill="var(--lime)"/>
    <!-- chart -->
    <g fill="var(--ink)">
      <rect x="347" y="391" width="3.5" height="6"/><rect x="352" y="388" width="3.5" height="9"/>
      <rect x="357" y="384" width="3.5" height="13"/><rect x="362" y="380" width="3.5" height="17"/>
    </g>
    <path d="M346 386l8-6 5 3 9-8" fill="none" stroke="var(--ink)" stroke-width="1.6"/>
    <path d="M365 374h4v4z" fill="var(--ink)"/>
    <!-- chat -->
    <path d="M531 381h18a3 3 0 0 1 3 3v10a3 3 0 0 1-3 3h-11l-5 4v-4h-2a3 3 0 0 1-3-3v-10a3 3 0 0 1 3-3z" fill="var(--ink)"/>
    <rect x="535" y="386" width="10" height="1.6" fill="var(--lime)"/>
    <rect x="535" y="390" width="7" height="1.6" fill="var(--lime)"/>
    <path d="M553 374l1.3 2.8 3 .3-2.3 2 .7 3-2.7-1.6-2.7 1.6.7-3-2.3-2 3-.3z" fill="var(--ink)"/>
  </svg>

  <div class="block block--left" style="top:142px">
    <h3>Starting Point &amp;<span>Goal</span></h3>
    <p>A retail company was evaluating several new locations. The question was: How would transportation costs and customer delivery change with a move?</p>
  </div>
  <div class="block block--right" style="top:142px">
    <h3>The solution<span>– Our simulation</span></h3>
    <p>We combined location data, customer addresses, and delivery quantities with an automated route planner. This allowed us to calculate and visualize the new transport costs and travel times for all variants.</p>
  </div>
  <div class="block block--left" style="top:329px">
    <h3>The Concrete<span>Benefit</span></h3>
    <p>Comparison of locations with actual routes<br>Transparent calculation of transport costs<br>Clear decision-making basis for management<br>First results in less than 3 weeks</p>
  </div>
  <div class="block block--right" style="top:329px">
    <h3>Customer<span>Feedback</span></h3>
    <p>“We knew exactly which location was most efficient for our customer deliveries – data-based and traceable.”</p>
  </div>

  <div class="footer">
    <span class="cta-label">Test now:</span> Secure your location decision with simulation
    <div class="contact">
      <span class="item"><svg width="8" height="8" viewBox="0 0 24 24"><path fill="var(--lime)" d="M6.6 10.8a15 15 0 0 0 6.6 6.6l2.2-2.2a1 1 0 0 1 1-.3 11 11 0 0 0 3.6.6 1 1 0 0 1 1 1V20a1 1 0 0 1-1 1A17 17 0 0 1 3 4a1 1 0 0 1 1-1h3.5a1 1 0 0 1 1 1 11 11 0 0 0 .6 3.6 1 1 0 0 1-.3 1z"/></svg>+41 44 000 12 34</span>
      <span class="sep"></span>
      <span class="item"><svg width="9" height="7" viewBox="0 0 24 18"><rect width="24" height="18" rx="2" fill="var(--lime)"/><path d="M1 2l11 8 11-8" fill="none" stroke="var(--black)" stroke-width="2"/></svg>info@kalvor.ch</span>
    </div>
  </div>
</section>

<section class="slide slide--results">
  <div class="accent"></div>
  <h1 class="slide-title">WHAT IF</h1>
  <div class="brand"><span class="brand-dot"></span><span class="brand-name">Kalvor</span></div>
  <h2 class="headline">YOU COULD COMPARE NEW LOCATIONS WITH REAL TRANSPORTATION COSTS?</h2>

  <figure class="shot shot--map"><div class="fill" role="img" aria-label="Map of Switzerland with customer and location markers"></div></figure>
  <figure class="shot shot--dash"><div class="fill" role="img" aria-label="Route planning evaluation dashboard with route map, table and charts"></div></figure>

  <div class="footer">
    <span class="cta-label">Test now:</span> Secure your location decision with simulation
    <div class="contact">
      <span class="item"><svg width="8" height="8" viewBox="0 0 24 24"><path fill="var(--lime)" d="M6.6 10.8a15 15 0 0 0 6.6 6.6l2.2-2.2a1 1 0 0 1 1-.3 11 11 0 0 0 3.6.6 1 1 0 0 1 1 1V20a1 1 0 0 1-1 1A17 17 0 0 1 3 4a1 1 0 0 1 1-1h3.5a1 1 0 0 1 1 1 11 11 0 0 0 .6 3.6 1 1 0 0 1-.3 1z"/></svg>+41 44 000 12 34</span>
      <span class="sep"></span>
      <span class="item"><svg width="9" height="7" viewBox="0 0 24 18"><rect width="24" height="18" rx="2" fill="var(--lime)"/><path d="M1 2l11 8 11-8" fill="none" stroke="var(--black)" stroke-width="2"/></svg>info@kalvor.ch</span>
    </div>
  </div>
</section>

</body>
</html>
```